Kelvo Tech Oz Business card revamp

We are looking to revamp our business card design. We are hoping to change our colours to dark navey blue, gray, white and black but are open to keeping the same if a good design is submited. We are after somthing a bit differnt not just boring business card. I have attached a copy of our current card. We Want to keep the same logo design which i have attached a few to hopfully help you in this process. We are after a design that can be personalized to separate 4 people

Colors
0455a3
ffffff
000000
cbcbcb

Requirements
Must have
• Kelvo Tech Logo, address 3/41 Mallory Court, Wexhill 4218, phone number, Name and position

```html
<!DOCTYPE html>
<html lang="en">
<head>
<meta charset="utf-8">
<title>Kelvo Tech Oz – Business Card</title>
<link href="https://fonts.googleapis.com/css2?family=Arimo:ital,wght@0,400;0,700;1,400;1,700&display=swap" rel="stylesheet">
<style>
  :root {
    --brand-blue: #0b61b3;
    --brand-blue-deep: #0455a3;
    --accent-orange: #f0802a;
    --paper: #ffffff;
    --backdrop: #e9e9ea;
    --rule: rgba(255,255,255,0.75);
  }
  * { box-sizing: border-box; margin: 0; padding: 0; }
  html, body { width: 1200px; height: 800px; overflow: hidden; }
  body {
    background: var(--backdrop);
    font-family: "Arimo", Arial, sans-serif;
    position: relative;
  }
  .card {
    position: absolute;
    width: 525px;
    height: 300px;
    overflow: hidden;
    box-shadow: 0 6px 18px rgba(0,0,0,0.12);
  }

  /* Front: solid blue with wordmark */
  .card-front {
    left: 80px;
    top: 420px;
    background: var(--brand-blue);
    color: var(--paper);
  }
  .front-wordmark {
    position: absolute;
    left: 0; right: 0;
    top: 92px;
    text-align: center;
  }
  .wordmark-row {
    display: inline-flex;
    align-items: center;
    gap: 14px;
  }
  .wordmark-dot {
    width: 22px; height: 22px;
    border-radius: 50%;
    background: var(--paper);
  }
  .wordmark-name {
    font-weight: 700;
    font-size: 48px;
    letter-spacing: -0.5px;
    color: var(--paper);
  }
  .front-descriptor {
    margin-top: 4px;
    font-weight: 700;
    font-size: 19px;
    letter-spacing: 0.3px;
  }
  .front-slogan {
    position: absolute;
    left: 34px;
    right: 0;
    bottom: 48px;
    display: flex;
    align-items: center;
    gap: 12px;
    font-size: 14px;
    font-style: italic;
  }
  .front-slogan strong { font-weight: 700; }
  .front-slogan .slogan-rule {
    flex: 1;
    height: 1px;
    background: var(--rule);
  }
  .front-marker {
    position: absolute;
    left: 0;
    bottom: 70px;
    width: 16px;
    height: 22px;
    background: var(--accent-orange);
  }

  /* Back: white with blue swoosh and contact details */
  .card-back {
    left: 595px;
    top: 80px;
    background: var(--paper);
  }
  .card-back .swoosh {
    position: absolute;
    inset: 0;
    width: 100%;
    height: 100%;
  }
  .back-wordmark {
    position: absolute;
    left: 40px;
    top: 62px;
    display: flex;
    align-items: center;
    gap: 10px;
  }
  .back-wordmark .wordmark-dot { background: var(--accent-orange); width: 16px; height: 16px; }
  .back-wordmark .wordmark-name { color: var(--brand-blue); font-size: 34px; }
  .back-descriptor {
    position: absolute;
    left: 40px;
    top: 104px;
    font-weight: 700;
    font-size: 13px;
    color: var(--brand-blue);
  }
  .contact {
    position: absolute;
    left: 330px;
    top: 118px;
    color: var(--paper);
  }
  .contact-name { font-weight: 700; font-size: 19px; }
  .contact-role { font-size: 14px; margin-top: 2px; }
  .contact-rule { width: 26px; height: 1px; background: var(--paper); margin: 12px 0 10px; }
  .contact-line {
    display: flex;
    align-items: flex-start;
    gap: 8px;
    font-size: 13.5px;
    line-height: 1.35;
  }
  .contact-line svg { flex: none; margin-top: 2px; }
</style>
</head>
<body>

  <section class="card card-front" aria-label="Card front">
    <div class="front-wordmark">
      <div class="wordmark-row">
        <span class="wordmark-dot"></span>
        <span class="wordmark-name">Kelvo Tech</span>
      </div>
      <div class="front-descriptor">Passive Fire Protection</div>
    </div>
    <span class="front-marker"></span>
    <p class="front-slogan">
      <span>Reliability with <strong>Dedication to Service</strong></span>
      <span class="slogan-rule"></span>
    </p>
  </section>

  <section class="card card-back" aria-label="Card back">
    <svg class="swoosh" viewBox="0 0 525 300" preserveAspectRatio="none" aria-hidden="true">
      <path d="M300 0 C 330 120, 260 240, 110 300 L 525 300 L 525 0 Z" fill="var(--accent-orange)"/>
      <path d="M318 0 C 345 125, 280 245, 140 300 L 525 300 L 525 0 Z" fill="var(--brand-blue)"/>
    </svg>

    <div class="back-wordmark">
      <span class="wordmark-dot"></span>
      <span class="wordmark-name">Kelvo Tech</span>
    </div>
    <div class="back-descriptor">Passive Fire Protection</div>

    <div class="contact">
      <div class="contact-name">Daniel Marsh</div>
      <div class="contact-role">Managing Director</div>
      <div class="contact-rule"></div>
      <div class="contact-line">
        <svg width="11" height="12" viewBox="0 0 24 24" aria-hidden="true"><path fill="#fff" d="M6.6 10.8a15 15 0 0 0 6.6 6.6l2.2-2.2c.3-.3.7-.4 1-.2 1.1.4 2.3.6 3.6.6.6 0 1 .4 1 1V20c0 .6-.4 1-1 1A17 17 0 0 1 3 4c0-.6.4-1 1-1h3.5c.6 0 1 .4 1 1 0 1.3.2 2.5.6 3.6.1.3 0 .7-.2 1z"/></svg>
        <span>(+61) 07 5550 1234</span>
      </div>
      <div class="contact-line">
        <svg width="11" height="12" viewBox="0 0 24 24" aria-hidden="true"><path fill="#fff" d="M12 2a7 7 0 0 0-7 7c0 5.2 7 13 7 13s7-7.8 7-13a7 7 0 0 0-7-7zm0 9.5A2.5 2.5 0 1 1 12 6.5a2.5 2.5 0 0 1 0 5z"/></svg>
        <span>3/41 Mallory Court<br>Wexhill 4218</span>
      </div>
    </div>
  </section>

</body>
</html>
```